Digital agency needs a new web design

We’re looking to redesign our website – so that it is 3 things: smart, stylish and simplistic.
Plinth are a digital performance agency, offering services in PPC. SEO. Analytics, Display, Content and Paid Social, and we work with fantastic clients.
Our current website isn't reflective of how forward-thinking we are as an agency, and doesn't convey our two USPs well - our technology and our network of digital marketing experts. So we're looking to build a clear and concise site that attracts both inbound leads and digital marketing professionals to join our team or our Plinthie network.
You can take a look at our current website here - http://plinth-example.net/. The copy will change and we happy for the colours to change.

Target Market(s)

The primary target audience is marketing directors, digital directors, marketing managers and online acquisition managers. The secondary audience are people in the industry looking for work either as permanent employees or as part of the Plinth freelance network.

Industry/Entity Type

Marketing

Number of Pages Required

5+ page

Font styles to use
Sans Serif

Requirements
Must have
• - A stylish/ grown-up feel
• - Be of a design/ templates that can be editable
• - A really clear concise/ homepage
• The homepage must include:
• 1. A reference to our services
• 2. A reference to our network of digital marketing experts
• 3. A reference to our technology
• 4. A section for case studies
• 5. A section for our blog
• 6. A newsletter signup
• Th copy will be changed so please don't feel like you need to keep that.
Should not have
• - Cartoon style images as on the site on the moment
• - You should not have to scroll very far to find out what we do

```html
<!DOCTYPE html>
<html lang="en">
<head>
<meta charset="utf-8">
<title>Plinth – Digital Performance Agency</title>
<link href="https://fonts.googleapis.com/css2?family=Oswald:wght@400;500&family=Roboto:wght@400;500;700&display=swap" rel="stylesheet">
<style>
:root{
  --yellow:#fcd04f;
  --yellow-deep:#f5c33b;
  --gold:#c9a233;
  --ink:#1c1c1c;
  --black:#000;
  --white:#fff;
  --grey-band:#e6e6e6;
  --text:#2a2a2a;
  --muted:#555;
  --navy:#1d2f55;
  --navy-deep:#0f1a33;
  --card-dark:#2b2f33;
}
*{box-sizing:border-box;margin:0;padding:0}
html,body{width:1200px;height:3523px;overflow:hidden}
body{font-family:"Roboto",sans-serif;color:var(--text);background:var(--white);position:relative}
.abs{position:absolute}
.oswald{font-family:"Oswald",sans-serif}

/* header + hero */
.hero{position:absolute;left:0;top:0;width:1200px;height:615px;
  background:linear-gradient(160deg,#2c4a7d 0%,var(--navy) 45%,var(--navy-deep) 100%)}
.hero-photo{position:absolute;inset:0;background:radial-gradient(ellipse at 70% 35%,rgba(120,150,200,.45),transparent 60%)}
.topbar{position:absolute;left:0;top:0;width:1200px;height:113px;background:rgba(10,18,36,.55);border-bottom:4px solid var(--yellow)}
.brand{font-family:"Roboto",sans-serif;font-weight:500;color:var(--white);font-size:40px;letter-spacing:.5px}
.social{display:flex;gap:14px}
.social span{width:24px;height:24px;border-radius:50%;background:rgba(255,255,255,.18)}
.social span.on{background:var(--yellow)}
.phone{color:var(--white);font-size:15px;font-weight:500;display:flex;align-items:center;gap:8px}
.mainnav{display:flex;gap:36px;color:var(--white);font-size:15px;font-weight:500;text-transform:uppercase}
.hero-title{left:0;width:1200px;text-align:center}
.hero-title .boxed{display:inline-block;background:var(--yellow);color:var(--ink);font-family:"Oswald",sans-serif;font-size:56px;padding:4px 22px;line-height:1.2}
.hero-title .plain{font-family:"Oswald",sans-serif;color:var(--white);font-size:56px;line-height:1.2;margin-top:4px}

/* welcome */
.welcome{position:absolute;left:0;top:615px;width:1200px;height:449px;background:var(--yellow)}
.section-title{font-family:"Oswald",sans-serif;font-size:34px;color:var(--ink);text-transform:uppercase;text-align:center;width:1200px;left:0}
.welcome p{left:160px;width:880px;text-align:center;font-size:15.5px;line-height:2.3;color:var(--ink)}
.pillars{left:146px;width:920px;display:grid;grid-template-columns:1fr 1fr;row-gap:22px;font-size:15px;color:var(--ink)}
.pillars li{list-style:none;display:flex;align-items:center;gap:12px}
.pillars li::before{content:"";width:14px;height:14px;border-radius:50%;background:var(--ink)}
.connector{width:2px;background:var(--ink)}
.connector::after{content:"";position:absolute;left:-4px;bottom:-5px;width:10px;height:10px;border-radius:50%;background:var(--ink)}

/* services */
.services{position:absolute;left:0;top:1064px;width:1200px;height:429px;background:var(--grey-band)}
.service{width:250px;text-align:center}
.service .icon{width:80px;height:80px;margin:0 auto;border-radius:50%;background:#cfcfcf}
.service h3{font-size:20px;font-weight:500;color:var(--ink);margin-top:34px}
.service p{font-size:13.5px;line-height:1.95;color:var(--muted);margin-top:10px}

/* blog + news */
.label{font-family:"Oswald",sans-serif;font-size:23px;color:var(--ink);text-transform:uppercase;left:99px}
.tile{position:absolute;overflow:hidden;background:linear-gradient(150deg,#4a4f55,var(--card-dark))}
.tile .shade{position:absolute;inset:0;background:rgba(0,0,0,.55)}
.tile .txt{position:absolute;left:18px;right:16px;top:18px;color:var(--white);font-size:14.5px;font-weight:500;line-height:1.75}
.tile .date{font-size:13px;margin-bottom:10px;display:block}
.band{position:absolute;left:0;right:0;bottom:0;height:82px;padding:18px 18px;color:var(--white)}
.band .date{font-size:13px;font-weight:500}
.band h4{font-size:19px;font-weight:500;text-transform:uppercase;margin-top:10px}
.play{position:absolute;width:76px;height:76px;border:4px solid var(--white);border-radius:50%}
.play::after{content:"";position:absolute;left:28px;top:20px;border-left:24px solid var(--white);border-top:14px solid transparent;border-bottom:14px solid transparent}

/* cta */
.cta{position:absolute;left:0;top:2376px;width:1200px;height:395px;background:linear-gradient(120deg,#3a3a3a,#1b1b1b 60%,#2c2c2c)}
.cta .veil{position:absolute;inset:0;background:rgba(0,0,0,.45)}
.cta h2{font-family:"Oswald",sans-serif;font-weight:400;font-size:38px;color:var(--white);text-align:center;width:1200px;left:0;top:62px}
.cta p{color:var(--white);font-size:18px;font-weight:500;line-height:2.1;text-align:center;left:200px;width:800px;top:172px}
.btn-join{left:533px;top:282px;width:139px;height:45px;border:2px solid var(--white);background:var(--gold);color:var(--white);font-size:16px;font-weight:500;text-transform:uppercase;display:flex;align-items:center;justify-content:center}

/* contact */
.contact{position:absolute;left:0;top:2771px;width:1200px;height:427px;background:#dde3d6}
.form-title{font-family:"Oswald",sans-serif;font-size:23px;color:var(--ink);left:578px;top:48px}
.field{position:absolute;width:256px;height:45px;border:2px solid #5c4a14;font-size:14.5px;color:var(--ink);padding:0 10px;display:flex;align-items:center}
.field.tall{height:96px;align-items:flex-start;padding-top:11px}
.field.select{justify-content:space-between}
.send{position:absolute;left:578px;top:317px;width:256px;height:44px;background:var(--black);color:var(--white);font-size:14px;font-weight:500;display:flex;align-items:center;justify-content:center}

/* footer */
.footer{position:absolute;left:0;top:3198px;width:1200px;height:325px;background:var(--black);color:var(--white)}
.footnav{left:0;width:1200px;top:188px;display:flex;justify-content:center;gap:22px;font-size:16px;font-weight:700;text-transform:uppercase}
.footnav .sep{font-weight:400}
.rule{left:99px;width:1002px;top:234px;height:1px;background:#444}
.copy{left:99px;top:276px;font-size:13px}
.foot-social{left:909px;top:266px;display:flex;gap:10px}
.foot-social span{width:32px;height:32px;border:2px solid var(--white);border-radius:50%}
</style>
</head>
<body>

<header class="hero">
  <div class="hero-photo" role="img" aria-label="Photo of hands working on a laptop with digital performance charts overlaid"></div>
  <div class="topbar">
    <div class="abs brand" style="left:99px;top:28px">Plinth</div>
    <div class="abs social" style="left:720px;top:16px"><span></span><span class="on"></span><span></span><span></span><span></span></div>
    <div class="abs phone" style="left:905px;top:17px">
      <svg width="14" height="14" viewBox="0 0 24 24"><path fill="#fff" d="M6.6 10.8a15 15 0 0 0 6.6 6.6l2.2-2.2a1 1 0 0 1 1-.25 11.4 11.4 0 0 0 3.6.57 1 1 0 0 1 1 1V20a1 1 0 0 1-1 1A17 17 0 0 1 3 4a1 1 0 0 1 1-1h3.5a1 1 0 0 1 1 1c0 1.25.2 2.45.57 3.57a1 1 0 0 1-.25 1z"/></svg>
      UK: +44 20 7946 0185
    </div>
    <nav class="abs mainnav" style="left:521px;top:70px">
      <span>Home</span><span>About Plinth</span><span>Our Work</span><span>Blog</span><span>Join Us</span><span>Contact</span>
    </nav>
  </div>
  <div class="abs hero-title" style="top:212px">
    <div class="boxed">DIGITAL PERFORMANCE</div>
    <div class="plain">RE - INVENTED</div>
  </div>
  <div class="play" style="left:558px;top:402px"></div>
  <svg class="abs" style="left:588px;top:541px" width="24" height="40" viewBox="0 0 24 40"><rect x="2" y="2" width="20" height="36" rx="10" fill="none" stroke="#fff" stroke-width="2"/><line x1="12" y1="9" x2="12" y2="16" stroke="#fff" stroke-width="2"/></svg>
</header>

<section class="welcome">
  <div class="abs connector" style="left:600px;top:0;height:42px"></div>
  <h2 class="abs section-title" style="top:80px">Welcome to Plinth</h2>
  <p class="abs" style="top:170px">Our mission is to build the worlds greatest performance digital agency. In our experience, there is no such thing as a great agency, just great people in search agencies, so we have built an agency that focuses on 4 key pillars:</p>
  <ul class="abs pillars" style="top:290px">
    <li>Great people</li>
    <li>Everyone should own a share</li>
    <li>Supported by our very own network of digital marketing experts</li>
    <li>Technology should enhance everything that we do</li>
  </ul>
  <div class="abs connector" style="left:600px;top:410px;height:34px"></div>
</section>

<section class="services">
  <h2 class="abs section-title" style="top:40px">Our Services</h2>
  <div class="abs service" style="left:101px;top:160px"><div class="icon" role="img" aria-label="PPC service icon"></div><h3>PPC</h3><p>Within your timeline you'll see everything that we're working on, what tasks we have in line.</p></div>
  <div class="abs service" style="left:350px;top:160px"><div class="icon" role="img" aria-label="SEO service icon"></div><h3>SEO</h3><p>Within your timeline you'll see everything that we're working on, what tasks we have in line.</p></div>
  <div class="abs service" style="left:600px;top:160px"><div class="icon" role="img" aria-label="Display service icon of a monitor"></div><h3>DISPLAY</h3><p>Within your timeline you'll see everything that we're working on, what tasks we have in line.</p></div>
  <div class="abs service" style="left:848px;top:160px"><div class="icon" role="img" aria-label="Analytics service icon of a rising chart on screen"></div><h3>ANALYTICS</h3><p>Within your timeline you'll see everything that we're working on, what tasks we have in line.</p></div>
</section>

<section class="blog">
  <h3 class="abs label" style="top:1523px">Recent posts from blog:</h3>
  <div class="tile" style="left:99px;top:1573px;width:483px;height:336px;background:linear-gradient(120deg,#c47a3a,#8a5634 50%,#5e4a3d)" role="img" aria-label="Team of colleagues discussing work together">
    <div class="play" style="left:202px;top:90px"></div>
    <div class="band" style="background:rgba(40,40,40,.85)"><div class="date">01.08.2016</div><h4>You see every piece of work</h4></div>
  </div>
  <div class="tile" style="left:585px;top:1573px;width:256px;height:336px" role="img" aria-label="Person typing at a desk">
    <div class="shade"></div>
    <div class="txt"><span class="date">01.08.2016</span>Within your timeline you'll see everything that we're working on, what tasks we have in line to do next and what we've delivered for your business.</div>
  </div>
  <div class="tile" style="left:843px;top:1573px;width:258px;height:336px" role="img" aria-label="Office workspace with a person at a computer">
    <div class="shade"></div>
    <div class="txt"><span class="date">01.08.2016</span>Plinth will become a part of your marketing team and that means visibility on all channels and other media. We'll ensure that campaign are integrated.</div>
  </div>

  <h3 class="abs label" style="top:1942px">News and articles:</h3>
  <div class="tile" style="left:99px;top:1996px;width:258px;height:333px" role="img" aria-label="Hands holding a tablet showing charts">
    <div class="shade"></div>
    <div class="txt"><span class="date">01.08.2016</span>No plan, no direction, no success. As part of an account development plan and after gaining a clear understanding of your goals and audience.</div>
  </div>
  <div class="tile" style="left:359px;top:1996px;width:256px;height:333px" role="img" aria-label="Laptop on a desk with a notebook">
    <div class="shade"></div>
    <div class="txt"><span class="date">01.08.2016</span>We pride ourselves in being a performance-driven agency, one that brings change to your business and does so efficiently.</div>
  </div>
  <div class="tile" style="left:617px;top:1996px;width:484px;height:333px;background:linear-gradient(130deg,#8a9096,#5c6268 55%,#a0764a)" role="img" aria-label="Person using a tablet in a busy shop">
    <div class="play" style="left:204px;top:80px"></div>
    <div class="band" style="background:rgba(252,208,79,.9);height:86px;padding-top:26px"><div class="date">01.08.2016</div><h4 style="margin-top:6px">With a media schedule</h4></div>
  </div>
</section>

<section class="cta" role="img" aria-label="Dimmed photo of people working in a library office">
  <div class="veil"></div>
  <h2 class="abs">WHAT'S THE PLINTH WEBSITE FOR?</h2>
  <p class="abs">The primary goal of the site is to generate appropriate incoming leads to the business. The secondary goal is to attract employees to the business.</p>
  <div class="abs btn-join">Join Us</div>
</section>

<section class="contact">
  <div class="abs" style="left:0;top:0;width:1200px;height:427px;background:linear-gradient(135deg,#e8ebe2,#cfd8c6 60%,#d9dfd2)" role="img" aria-label="Street map of the office location"></div>
  <svg class="abs" style="left:0;top:0" width="1200" height="427" viewBox="0 0 1200 427"><polygon points="530,0 1200,0 1200,427 900,427 870,330" fill="#fcd04f"/></svg>
  <h3 class="abs form-title">SEND US A MESSAGE:</h3>
  <div class="field" style="left:578px;top:103px">Your Name</div>
  <div class="field select" style="left:843px;top:103px">Please select one
    <svg width="10" height="6" viewBox="0 0 10 6"><path d="M0 0h10L5 6z" fill="#1c1c1c"/></svg></div>
  <div class="field" style="left:578px;top:152px">Company Name</div>
  <div class="field tall" style="left:843px;top:152px">Your Message</div>
  <div class="field" style="left:578px;top:204px">Work Email</div>
  <div class="field" style="left:578px;top:256px">Phone</div>
  <div class="field" style="left:843px;top:256px">What comes first, c or y?</div>
  <div class="send">SEND NOW</div>
</section>

<footer class="footer">
  <div class="abs brand" style="left:0;width:1200px;text-align:center;top:70px;font-size:50px">Plinth</div>
  <nav class="abs footnav">
    <span>Home</span><span class="sep">|</span><span>Services</span><span class="sep">|</span><span>About Plinth</span><span class="sep">|</span><span>Our Work</span><span class="sep">|</span><span>Blog</span><span class="sep">|</span><span>Contact</span>
  </nav>
  <div class="abs rule"></div>
  <div class="abs copy">© 2016 Plinth. All Rights Reserved</div>
  <div class="abs foot-social"><span></span><span></span><span></span><span></span><span></span></div>
</footer>

</body>
</html>
```